Web form face-lift for an online startup

We are a web startup building a SaaS application for the Ostrival Freight. The project is mainly dedicated to the paint the main form that our customer are using along the search results that the they get. All details are in the attached documents.
Updates
The application serves the Freight Forwarders community so please think towards this industry when using background images, banners, colors, icons, etc. Computer and technology images are irrelevant.
Customer fields at the top of the page is actually part of the form.
Target Market(s)
Usually business users (Sales people, procurement, shippers, freight forwarders). Some are less tech savvy and some appreciate the new trendy web apps.
Industry/Entity Type
Building
Colors
Designer to choose colors to be used in the design.
Look and feel
Each slider illustrates characteristics of the customer's brand and the style your logo design should communicate.

```html
<!DOCTYPE html>
<html lang="en">
<head>
<meta charset="utf-8">
<title>Ostrival Freight – Freight Quote Search</title>
<link rel="stylesheet" href="https://fonts.googleapis.com/css2?family=Arimo:wght@400;700&family=Tinos:wght@400&display=swap">
<style>
:root{
  --blue:#4a98cb;
  --blue-text:#3a8cc4;
  --dark:#333333;
  --ink:#2b2b2b;
  --muted:#6d6d6d;
  --panel:#f7f7f7;
  --line:#e4e4e4;
  --white:#ffffff;
}
*{box-sizing:border-box;margin:0;padding:0}
html,body{width:1200px;height:1071px;overflow:hidden;background:var(--white)}
body{position:relative;font-family:"Arimo",Arial,sans-serif;color:var(--ink)}
.abs{position:absolute}
.serif{font-family:"Tinos","Times New Roman",serif}

/* header */
.brand{left:173px;top:28px;font-size:34px;color:var(--blue-text);white-space:nowrap}
.utility{top:9px;font-size:11px;color:#8a8a8a;display:flex;align-items:center;gap:6px;white-space:nowrap}
.utility svg{width:16px;height:16px}
.phone{font-size:13px;font-weight:700;color:#7a7a7a}
.nav{top:50px;font-size:13px;color:var(--ink)}
.nav.active{color:var(--blue-text);border-bottom:2px solid var(--blue-text);padding-bottom:4px}

/* hero */
.hero{left:0;top:85px;width:1200px;height:292px;background:linear-gradient(180deg,#c9dff3 0%,#7fa7cf 35%,#5d8ab8 65%,#8fb1d3 100%)}
.hero-title{left:190px;top:126px;font-size:41px;color:var(--white);letter-spacing:1px;white-space:nowrap;text-shadow:0 1px 3px rgba(0,0,0,.35)}
.search-shell{left:171px;top:181px;width:479px;height:90px;background:rgba(40,45,55,.85)}
.search-input{left:189px;top:204px;width:300px;height:45px;background:var(--white);font-size:12px;color:#9a9a9a;padding:15px 17px}
.search-btn{left:495px;top:204px;width:137px;height:45px;background:var(--blue);color:var(--white);font-size:16px;text-align:center;line-height:45px}
.rate{left:190px;top:281px;font-size:15px;font-weight:700;color:var(--white);display:flex;align-items:center;gap:6px}
.rate-note{left:212px;top:300px;width:428px;font-size:12px;line-height:14px;color:var(--white)}

/* freight selector */
.select-title{left:173px;top:406px;font-size:33px;color:var(--ink);white-space:nowrap}
.select-title span{color:var(--blue-text)}
.select-note{left:173px;top:448px;width:280px;font-size:11px;line-height:14px;color:var(--muted)}
.card-active{left:477px;top:386px;width:159px;height:127px;background:#f9f9f9;border:1px solid var(--line);border-bottom:none}
.thumb{border:1px solid #d5d5d5}
.card-label{left:477px;top:487px;width:159px;text-align:center;font-size:12px;font-weight:700}
.more{left:915px;top:408px;width:114px;height:77px;background:var(--blue);color:var(--white);font-size:15px;text-align:center;line-height:77px}

/* form */
.form-panel{left:0;top:513px;width:1200px;height:310px;background:var(--panel);border-top:1px solid var(--line);border-bottom:1px solid var(--line)}
.route{height:58px;display:flex;font-size:13px}
.route-tag{background:var(--blue);color:var(--white);font-weight:700;display:flex;align-items:center;gap:26px;padding-left:16px}
.route-field{background:var(--dark);color:var(--white);flex:1;display:flex;align-items:center;padding-left:25px}
.field-label{top:629px;font-size:12px;font-weight:700;color:#444;text-align:center}
.field{top:653px;height:37px;background:var(--dark);color:var(--white);font-size:13px;display:flex;align-items:center;justify-content:center;gap:14px}
.field.blue{background:var(--blue)}
.check{width:20px;height:20px}
.opt-head{left:172px;top:718px;font-size:12px;font-weight:700;color:#444}
.opt{font-size:13px;display:flex;align-items:center;gap:8px}
.opt .blue{color:var(--blue-text)}
.divider{left:580px;top:714px;width:1px;height:94px;background:#dcdcdc}
.total-head{left:612px;top:718px;font-size:12px;font-weight:700;color:#444}
.total{top:740px;height:37px;color:var(--white);font-size:13px;display:flex;align-items:center;justify-content:center;background:var(--dark)}
.total.blue{background:var(--blue)}
.quote-btn{left:444px;top:846px;width:311px;height:61px;display:flex}
.quote-btn .txt{width:229px;background:var(--dark);color:var(--white);font-size:13px;display:flex;align-items:center;justify-content:center}
.quote-btn .ico{flex:1;background:var(--blue);display:flex;align-items:center;justify-content:center}

/* footer */
.band{left:0;top:933px;width:1200px;height:87px;background:linear-gradient(90deg,#2a3444 0%,#3c4757 25%,#222b37 55%,#1d2530 100%)}
.band-name{left:603px;top:952px;font-size:41px;color:var(--white);letter-spacing:1px;white-space:nowrap}
.copyright{left:172px;top:1039px;font-size:13px;color:#555}
.social{top:1039px;width:14px;height:14px;border-radius:50%;background:#666}
</style>
</head>
<body>

<header>
  <div class="abs brand serif">Ostrival Freight</div>
  <div class="abs utility" style="left:562px">
    <svg viewBox="0 0 16 16"><circle cx="8" cy="8" r="7" fill="#b5b5b5"/><path d="M8 8 L12 5" stroke="#fff" stroke-width="1.5"/></svg>Dashboard
  </div>
  <div class="abs utility" style="left:667px">
    <svg viewBox="0 0 16 16"><rect x="3" y="2" width="11" height="12" fill="none" stroke="#999" stroke-width="1.3"/><path d="M1 8h8M6 5l3 3-3 3" fill="none" stroke="#999" stroke-width="1.3"/></svg>Sign In
  </div>
  <div class="abs utility" style="left:752px">
    <svg viewBox="0 0 20 14" style="width:20px;height:14px"><rect width="20" height="14" fill="#c5c5c5"/><path d="M0 0L20 14M20 0L0 14" stroke="#eee" stroke-width="2"/><path d="M10 0v14M0 7h20" stroke="#eee" stroke-width="3"/></svg>English ⌄
  </div>
  <div class="abs utility" style="left:855px">
    <svg viewBox="0 0 16 16"><rect x="2" y="3" width="12" height="8" fill="none" stroke="#aaa" stroke-width="1.3"/><rect x="4" y="7" width="12" height="7" fill="#fff" stroke="#aaa" stroke-width="1.3"/></svg>$ ⌄
  </div>
  <div class="abs utility phone" style="left:920px">
    <svg viewBox="0 0 16 16"><path d="M4 2l2 3-1.5 1.5c1 2 3 4 5 5L11 10l3 2-1 2.5C8 15 1 8 1.5 3z" fill="#999"/></svg>0800-555-0192
  </div>
  <nav>
    <div class="abs nav active" style="left:562px">HOME</div>
    <div class="abs nav" style="left:629px">FREIGHT</div>
    <div class="abs nav" style="left:713px">ABOUT</div>
    <div class="abs nav" style="left:786px">INDUSTRY</div>
    <div class="abs nav" style="left:878px">SERVICES</div>
    <div class="abs nav" style="left:969px">CONTACT</div>
  </nav>
</header>

<section>
  <div class="abs hero" role="img" aria-label="Photo of a loaded container ship crossing a calm blue sea"></div>
  <h1 class="abs hero-title serif" style="font-weight:400">SEARCH THE QUOTE !</h1>
  <div class="abs search-shell"></div>
  <div class="abs search-input">Enter Your Keywords Here...</div>
  <div class="abs search-btn">SEARCH</div>
  <div class="abs rate">
    <svg width="17" height="17" viewBox="0 0 17 17"><rect x="1" y="1" width="15" height="15" fill="#fff"/><path d="M4 9l3 3 6-8" fill="none" stroke="#3a8cc4" stroke-width="2.2"/></svg>Rate quote ?
  </div>
  <p class="abs rate-note">Lorem ipsum dolor sit amet, consectetuer adipiscing elit, sed diam nonummy nibh euismod tin....</p>
</section>

<section>
  <h2 class="abs select-title serif" style="font-weight:400">Select your <span>freight</span> !</h2>
  <p class="abs select-note">Lorem ipsum dolor sit amet, consectetuers ddsda adipiscing elit, sed diam nonummy n euismodtin....</p>
  <div class="abs card-active"></div>
  <div class="abs thumb" style="left:500px;top:399px;width:114px;height:77px;background:linear-gradient(180deg,#5b4a3d,#b39a7b)" role="img" aria-label="Photo of a warehouse with boxes on pallets"></div>
  <div class="abs card-label">BOXES/PALLETS</div>
  <div class="abs thumb" style="left:653px;top:408px;width:114px;height:77px;background:linear-gradient(180deg,#9cc3e8,#4b7fb3)" role="img" aria-label="Photo of a container ship at sea"></div>
  <div class="abs thumb" style="left:784px;top:408px;width:114px;height:77px;background:linear-gradient(180deg,#6a5a48,#9b8a70)" role="img" aria-label="Photo of warehouse racks with a forklift"></div>
  <div class="abs more">MORE</div>
</section>

<section>
  <div class="abs form-panel"></div>

  <div class="abs route" style="left:171px;top:543px;width:405px">
    <div class="route-tag" style="width:134px">
      <svg width="16" height="22" viewBox="0 0 16 22"><path d="M8 0C3.6 0 0 3.5 0 8c0 6 8 14 8 14s8-8 8-14c0-4.5-3.6-8-8-8z" fill="#1f5f8a"/><circle cx="8" cy="8" r="3" fill="#4a98cb"/></svg>FROM
    </div>
    <div class="route-field">Shipping Address Or Port</div>
  </div>
  <svg class="abs" style="left:589px;top:562px" width="23" height="20" viewBox="0 0 23 20"><path d="M0 6h12V0l11 10-11 10v-6H0z" fill="#cfcfcf"/></svg>
  <div class="abs route" style="left:624px;top:543px;width:405px">
    <div class="route-tag" style="width:133px">
      <svg width="16" height="22" viewBox="0 0 16 22"><path d="M8 0C3.6 0 0 3.5 0 8c0 6 8 14 8 14s8-8 8-14c0-4.5-3.6-8-8-8z" fill="#1f5f8a"/><circle cx="8" cy="8" r="3" fill="#4a98cb"/></svg>TO
    </div>
    <div class="route-field">Shipping Address Or Port</div>
  </div>

  <div class="abs field-label" style="left:172px;width:101px">QTY</div>
  <div class="abs field-label" style="left:280px;width:60px">STACK</div>
  <div class="abs field-label" style="left:349px;width:133px">LOAD</div>
  <div class="abs field-label" style="left:491px;width:101px">LENGHT</div>
  <div class="abs field-label" style="left:600px;width:101px">WIDTH</div>
  <div class="abs field-label" style="left:710px;width:101px">HEIGHT</div>
  <div class="abs field-label" style="left:820px;width:101px">WEIGHT</div>
  <div class="abs field-label" style="left:927px;width:102px">ADD</div>

  <div class="abs field" style="left:172px;width:101px">05 <span style="color:#4a98cb;font-size:10px">⇕</span></div>
  <svg class="abs check" style="left:300px;top:661px" viewBox="0 0 20 20"><rect width="20" height="20" fill="#333"/><path d="M4 10l4 4 8-10" fill="none" stroke="#4a98cb" stroke-width="2.2"/></svg>
  <div class="abs field" style="left:349px;width:133px">Box / Pallet <span style="color:#4a98cb;font-size:10px">⌄</span></div>
  <div class="abs field" style="left:491px;width:101px">105 cm <span style="color:#4a98cb;font-size:10px">⇕</span></div>
  <div class="abs field" style="left:600px;width:101px">105 cm <span style="color:#4a98cb;font-size:10px">⇕</span></div>
  <div class="abs field" style="left:710px;width:101px">105 cm <span style="color:#4a98cb;font-size:10px">⇕</span></div>
  <div class="abs field" style="left:820px;width:101px">100 kg <span style="color:#4a98cb;font-size:10px">⇕</span></div>
  <div class="abs field blue" style="left:927px;width:102px">More Units</div>

  <div class="abs opt-head">OPTIONS</div>
  <div class="abs opt" style="left:172px;top:739px">
    <svg class="check" viewBox="0 0 20 20"><rect width="20" height="20" fill="#333"/><path d="M4 10l4 4 8-10" fill="none" stroke="#4a98cb" stroke-width="2.2"/></svg>Import</div>
  <div class="abs opt" style="left:317px;top:739px">
    <svg class="check" viewBox="0 0 20 20"><rect width="20" height="20" fill="#333"/></svg>Export</div>
  <div class="abs opt" style="left:465px;top:741px">Incoterm : <span class="blue">FCA</span></div>
  <div class="abs opt" style="left:172px;top:767px">
    <svg class="check" viewBox="0 0 20 20"><rect width="20" height="20" fill="#333"/><path d="M4 10l4 4 8-10" fill="none" stroke="#4a98cb" stroke-width="2.2"/></svg>
    <svg width="13" height="14" viewBox="0 0 13 14"><path d="M6.5 0L13 2.5C13 8 10 12 6.5 14 3 12 0 8 0 2.5z" fill="#4a98cb"/></svg>Safe</div>
  <div class="abs opt" style="left:317px;top:767px">
    <svg class="check" viewBox="0 0 20 20"><rect width="20" height="20" fill="#333"/><path d="M4 10l4 4 8-10" fill="none" stroke="#4a98cb" stroke-width="2.2"/></svg>
    <svg width="14" height="14" viewBox="0 0 14 14"><circle cx="7" cy="4" r="3.5" fill="#4a98cb"/><path d="M0 14c0-5 14-5 14 0z" fill="#4a98cb"/></svg>Gaurd</div>
  <div class="abs opt" style="left:469px;top:767px">
    <svg class="check" viewBox="0 0 20 20"><rect width="20" height="20" fill="#333"/><path d="M4 10l4 4 8-10" fill="none" stroke="#4a98cb" stroke-width="2.2"/></svg>
    <svg width="14" height="14" viewBox="0 0 14 14"><rect x="4" y="5" width="6" height="7" fill="#4a98cb"/><rect x="2" y="12" width="10" height="2" fill="#4a98cb"/><path d="M7 0v3M1 3l2 2M13 3l-2 2" stroke="#4a98cb" stroke-width="1.3"/></svg>Alert</div>

  <div class="abs divider"></div>
  <div class="abs total-head">TOTAL</div>
  <div class="abs total" style="left:612px;width:131px">02</div>
  <div class="abs total blue" style="left:754px;width:58px">CBM</div>
  <div class="abs total" style="left:812px;width:74px">01</div>
  <div class="abs total blue" style="left:896px;width:59px">KG</div>
  <div class="abs total" style="left:955px;width:74px">101</div>

  <div class="abs quote-btn">
    <div class="txt">Search For Quotes</div>
    <div class="ico"><svg width="30" height="30" viewBox="0 0 30 30"><circle cx="13" cy="13" r="10" fill="none" stroke="#fff" stroke-width="2"/><path d="M20.5 20.5L28 28" stroke="#fff" stroke-width="2.4"/></svg></div>
  </div>
</section>

<footer>
  <div class="abs band" role="img" aria-label="Dark banner photo of a container ship at dusk"></div>
  <div class="abs band-name serif">OSTRIVAL FREIGHT</div>
  <p class="abs copyright">Copyright © Ostrival Freight. All Right Reserved.</p>
  <div class="abs social" style="left:913px" aria-label="Social link"></div>
  <div class="abs social" style="left:940px" aria-label="Social link"></div>
  <div class="abs social" style="left:971px" aria-label="Social link"></div>
  <div class="abs social" style="left:1003px" aria-label="Social link"></div>
</footer>

</body>
</html>
```